Professional and creatice Life Coach - Business Card design

I just relaunched my website and now i a need a correspoonding business card for my task as life coach. My website is www.tbalrond.com as reference. The compass is kind of a symbol for my work, as I help people navigate through their challenging phases in life. The business card should be colorful, but not too playful as I also adress business people. So it sould be creative, but professional (also to suport my other business as Management Consultant)

Target Market(s)

People who want to get teir problems resolved, in business, partnership and other personal realms

Industry/Entity Type

Life Coaching

Contact Information for Business Card

Front side should include Name, Phone number, Email, Website and address

Font styles to use
Sans Serif

Colors
add136

Requirements
Must have
• "Mag. Leopold Brantner" -> Name
"Energetische Praxis" -> Jobtitle (describing my profession as life coach)
colours and style should match my website www.tbalrond.com
Nice to have
• a compass as a symbol

```html
<!DOCTYPE html>
<html lang="de">
<head>
<meta charset="utf-8">
<title>Business Card – Mag. Leopold Brantner</title>
<link rel="stylesheet" href="https://fonts.googleapis.com/css2?family=EB+Garamond:wght@400;500&family=Noto+Sans:wght@400&display=swap">
<style>
  :root {
    --bg: #e9e4dc;
    --forest: #37473a;
    --olive: #4e5f48;
    --lime: #bcd26c;
    --mist: #ececec;
    --paper: #f7f2f0;
    --ink: #2f3a31;
    --white: #ffffff;
  }
  html, body {
    margin: 0;
    width: 1200px;
    height: 1200px;
    overflow: hidden;
    background: var(--bg);
  }
  .stage {
    position: relative;
    width: 1200px;
    height: 1200px;
  }
  .card {
    position: absolute;
    left: 180px;
    width: 840px;
    height: 480px;
    box-shadow: 0 8px 24px rgba(0,0,0,.18);
  }
  .card svg { display: block; width: 840px; height: 480px; }
  .card--back { top: 90px; }
  .card--front { top: 630px; }
  .name { font-family: "EB Garamond", Georgia, serif; }
  .contact { font-family: "Noto Sans", Verdana, sans-serif; font-size: 20px; fill: var(--ink); letter-spacing: .5px; }
</style>
</head>
<body>
<div class="stage">

  <!-- Contact side -->
  <div class="card card--back">
    <svg viewBox="0 0 840 480" xmlns="http://www.w3.org/2000/svg">
      <defs>
        <linearGradient id="limeFade" x1="0" y1="0" x2="0" y2="1">
          <stop offset="0" stop-color="#bcd26c"/>
          <stop offset=".75" stop-color="#3e4f3c"/>
        </linearGradient>
        <linearGradient id="oliveFade" x1="0" y1="0" x2="0" y2="1">
          <stop offset="0" stop-color="#a9c160"/>
          <stop offset=".55" stop-color="#37473a"/>
        </linearGradient>
      </defs>
      <rect class="band-dark" width="840" height="480" fill="var(--forest)"/>
      <polygon points="0,0 390,0 350,80 370,140 330,240 300,300 230,480 0,480" fill="#bcd26c"/>
      <polygon points="110,0 360,0 370,150 330,250 300,290 120,40" fill="url(#oliveFade)"/>
      <polygon points="0,20 110,0 300,230 230,480 60,480 50,400 0,330" fill="url(#limeFade)"/>
      <polygon points="0,330 50,400 20,480 0,480" fill="var(--lime)"/>
      <polygon class="info-panel" points="350,215 840,195 840,480 210,480 300,300 330,300" fill="var(--mist)"/>
      <text class="name" x="420" y="100" font-size="34" fill="var(--white)">Mag. Leopold Brantner</text>
      <text class="name" x="422" y="145" font-size="24" fill="var(--white)">Energetische Praxis</text>

      <g class="contact-row">
        <circle cx="410" cy="265" r="22" fill="var(--forest)"/>
        <rect x="399" y="257" width="22" height="15" fill="none" stroke="var(--white)" stroke-width="2"/>
        <polyline points="399,257 410,266 421,257" fill="none" stroke="var(--white)" stroke-width="2"/>
        <text class="contact" x="448" y="272">user@email.com</text>
      </g>
      <g class="contact-row">
        <circle cx="415" cy="325" r="22" fill="var(--forest)"/>
        <path d="M405 314 l5 -2 4 8 -3 3 c2 4 5 7 9 9 l3 -3 8 4 -2 5 c-12 1 -25 -12 -24 -24z" fill="var(--white)"/>
        <text class="contact" x="453" y="332">333 3333 333</text>
      </g>
      <g class="contact-row">
        <circle cx="420" cy="385" r="22" fill="var(--forest)"/>
        <circle cx="420" cy="385" r="12" fill="none" stroke="var(--white)" stroke-width="1.6"/>
        <ellipse cx="420" cy="385" rx="5" ry="12" fill="none" stroke="var(--white)" stroke-width="1.4"/>
        <line x1="408" y1="385" x2="432" y2="385" stroke="var(--white)" stroke-width="1.4"/>
        <text class="contact" x="458" y="392">www.tbalrond.com</text>
      </g>
      <g class="contact-row">
        <circle cx="425" cy="445" r="22" fill="var(--forest)"/>
        <path d="M425 459 c-6 -8 -10 -13 -10 -18 a10 10 0 0 1 20 0 c0 5 -4 10 -10 18z" fill="none" stroke="var(--white)" stroke-width="2"/>
        <circle cx="425" cy="441" r="3.5" fill="var(--white)"/>
        <text class="contact" x="463" y="452">Address&#160;&#160;City, 1234</text>
      </g>
    </svg>
  </div>

  <!-- Name side -->
  <div class="card card--front">
    <svg viewBox="0 0 840 480" xmlns="http://www.w3.org/2000/svg">
      <defs>
        <linearGradient id="frontFade" x1="0" y1="0" x2="0" y2="1">
          <stop offset="0" stop-color="#bcd26c"/>
          <stop offset=".7" stop-color="#3e4f3c"/>
        </linearGradient>
        <linearGradient id="frontShade" x1="0" y1="0" x2="0" y2="1">
          <stop offset="0" stop-color="#4e5f48"/>
          <stop offset="1" stop-color="#3a4a3b"/>
        </linearGradient>
      </defs>
      <rect width="840" height="480" fill="var(--paper)"/>
      <polygon points="490,0 840,0 840,480 680,480 590,300 560,290 480,120 540,0" fill="url(#frontShade)"/>
      <polygon points="560,0 840,0 840,480 680,480 590,300 650,220 540,130" fill="url(#frontFade)"/>
      <polygon points="700,0 760,0 600,240 580,230" fill="#5c6e50" opacity=".5"/>
      <polygon points="840,330 840,470 800,480 770,420" fill="var(--lime)"/>

      <g class="brand-mark">
        <circle cx="170" cy="130" r="58" fill="var(--forest)"/>
        <text class="name" x="250" y="145" font-size="40" font-weight="500" fill="var(--forest)">Brantner</text>
      </g>

      <text class="name" x="85" y="330" font-size="44" font-weight="500" fill="var(--ink)">Mag. Leopold Brantner</text>
      <text class="name" x="85" y="375" font-size="30" fill="var(--ink)">Energetische Praxis</text>
    </svg>
  </div>

</div>
</body>
</html>
```